Scrap Metal Company Require Brochure for presentation to prospective client

We are a scrap metal company based in Singapore.
We require a brochure of about 4 pages, 1) Cover Page, 2 and 3 is the material we deal in and services we provide and 4) a backpage.
Brochure will be presented to prospective and selected local supplier to present to them the type of products we deal in and the type of services we provide. Purpose is to convince the prospective client to engage our services and also to sell us their scrap metal.
http://www.tarbelkow.com/our-services/for-corporate <- This link is for the intended audience of this brochure.
Designer is welcome to take any images from my website or use their own images in the design. Preferably, should the designer choose to use scrap metal images, please try to mainly use pictures of aluminium scrap, copper scrap, stainless steel scrap and ferrous scrap.
Attached is our company logo and some pictures of the scrap. www.tarbelkow.com is our website.
The design should give the audience a feeling of confidence, professionalism, honesty and trust in us.
This brochure is intended to be A4 Sizer
Target Market(s)
Local manufacturing company that does metal fabrication with off-cut scrap during the manufacturing process
Industry/Entity Type
Steel
Look and feel

```html
<!DOCTYPE html>
<html lang="en">
<head>
<meta charset="utf-8">
<title>Our Services – Tarbelkow Recycling</title>
<link href="https://fonts.googleapis.com/css2?family=Oswald:wght@300;400&display=swap" rel="stylesheet">
<style>
  :root {
    --paper: #ffffff;
    --ink: #3a3a3a;
    --ink-soft: #4a4a4a;
    --gold: #c9a24a;
    --gold-light: #efd9a0;
    --gold-dark: #a47b2c;
    --scrap-a: #8d96a3;
    --scrap-b: #c7ccd3;
    --scrap-c: #6b7482;
  }
  * { margin: 0; padding: 0; box-sizing: border-box; }
  html, body { width: 848px; height: 1200px; overflow: hidden; background: var(--paper); }
  .page {
    position: relative;
    width: 848px;
    height: 1200px;
    background: var(--paper);
    font-family: "Oswald", "Arial Narrow", sans-serif;
    font-weight: 300;
    color: var(--ink);
  }
  .hero-photo {
    position: absolute;
    left: 0; top: 0;
    width: 848px; height: 270px;
    background:
      radial-gradient(circle at 20% 40%, rgba(200,60,60,.35), transparent 35%),
      radial-gradient(circle at 65% 30%, rgba(230,200,60,.35), transparent 30%),
      radial-gradient(circle at 85% 70%, rgba(60,110,200,.3), transparent 30%),
      linear-gradient(160deg, var(--scrap-b), var(--scrap-a) 50%, var(--scrap-c));
  }
  .gold-band {
    position: absolute;
    left: 0; top: 270px;
    width: 848px; height: 6px;
    background: linear-gradient(90deg, var(--gold-dark), var(--gold-light) 30%, var(--gold) 60%, var(--gold-light) 85%, var(--gold-dark));
  }
  .content {
    position: absolute;
    left: 53px; top: 318px;
    width: 750px;
  }
  .title {
    font-weight: 300;
    font-size: 60px;
    line-height: 66px;
    letter-spacing: 0.5px;
    color: #222;
    text-transform: uppercase;
  }
  .intro p {
    font-size: 15px;
    line-height: 27px;
    color: var(--ink-soft);
  }
  .list-heading {
    font-size: 21px;
    line-height: 28px;
    margin-top: 12px;
    color: var(--ink-soft);
  }
  .item-list { list-style: none; }
  .item-list li {
    font-size: 15px;
    line-height: 27px;
    color: var(--ink-soft);
  }
  .item-list li::before { content: "- "; }
  .products-heading { margin-top: 20px; }
  .brand {
    position: absolute;
    left: 537px; top: 996px;
    width: 250px;
    text-align: center;
  }
  .brand-mark {
    display: block;
    width: 70px; height: 70px;
    margin: 0 auto 14px;
    border: 3px solid var(--gold);
  }
  .brand-name {
    font-weight: 400;
    color: var(--gold);
    font-size: 26px;
    line-height: 28px;
    letter-spacing: 1.5px;
  }
  .brand-sub {
    font-weight: 400;
    color: var(--gold);
    font-size: 15px;
    line-height: 18px;
    letter-spacing: 2px;
    text-align: right;
  }
</style>
</head>
<body>
<div class="page">
  <div class="hero-photo" role="img" aria-label="Photograph of compressed bales of crushed aluminium drink cans"></div>
  <div class="gold-band"></div>

  <div class="content">
    <h1 class="title">Our Services</h1>
    <div class="intro">
      <p>Tarbelkow Recycling provides one-stop scrap solutions for all levels, from international to corporate to individual.</p>
      <p>It has always been our priority to ensure continuous customer satisfaction and will do our utmost to meet our customer requirements. Our prices are review daily to ensure that our company purchase your scrap/recyclable at the most competitive pricing around in the market.</p>
      <p>Some of the services and products we deal in:</p>
    </div>

    <h2 class="list-heading">Services:</h2>
    <ul class="item-list">
      <li>Prompt On-site/Off-site quotation</li>
      <li>Hassle free disposal of scrap material</li>
      <li>On site weighing service</li>
      <li>Proof of destruction of scrap material (if required when sensitive data involved)</li>
      <li>Prompt Payment</li>
      <li>Provision of metal bins for the disposal of scrap</li>
    </ul>

    <h2 class="list-heading products-heading">Products:</h2>
    <ul class="item-list">
      <li>All types and grade of scrap</li>
      <li>All grades of aluminium/ stainless steel/ copper/ brass</li>
      <li>Electrical cables/wires</li>
      <li>Electronic components</li>
      <li>Used machinery</li>
      <li>Industrial surplus</li>
      <li>PCB board</li>
      <li>Precious metal</li>
      <li>All other recyclables products</li>
    </ul>
  </div>

  <div class="brand">
    <span class="brand-mark"></span>
    <div class="brand-name">TARBELKOW</div>
    <div class="brand-sub">RECYCLING</div>
  </div>
</div>
</body>
</html>
```